Postcard/Flyer design for Plastic Surgery Practice Open House
LVR Plastic Surgery Chicago
Postcard/Flyer design for Plastic Surgery Practice Open House - Medical
Creative Brief
Professional
Tomas R. Belvino, MD, FACS
Plastic, Reconstructive & Aesthetic Surgery
Harwick Medical Pavilion 2718 N. 61st Street Suite 305 Oak Lawn, IL 60917
belvinoMD@mailvexa.com
www.LVRplasticsurg.example
Spend an evening with Board Certified Plastic Surgeon, Dr. Tomas R. Belvino learning about the latest trends in Cosmetic Plastic Surgery. Bullets: Cosmetic Breast Surgery Mommy Makeovers Facial Aging Live Demonstrations Mini Consultations Discounts, Raffles, Giveaways ($500-$1000 savings) for booking your procedure. hors d'oeuvres will be served When: June 27, 2019 4p-6p Where: 2718 N. 61st Street Suite 305 Oak Lawn, IL 60917 Phone: (708) 555-0173 Please RSVP by June 14, 2019 to belvinoMD@mailvexa.com or DM on instagram @belvinoMD
(Instagram logo) @belvinoMD (Facebook logo) LVR Plastic Surgery
BelvinoMD BelvinoMD
All Contestants - I am not looking for a business card. I need a postcard to promote an event. Please see the comments in the initial design request.
Need a post card to promote an open house event for my Plastic Surgery Practice

```html
<!DOCTYPE html>
<html lang="en">
<head>
<meta charset="utf-8">
<title>LVR Plastic Surgery – Open House Postcard</title>
<link href="https://fonts.googleapis.com/css2?family=Libre+Baskerville&family=Raleway:ital,wght@0,400;1,400&family=Poppins:wght@400&display=swap" rel="stylesheet">
<style>
  :root {
    --bg: #e9e8e5;
    --card-dark: #232323;
    --card-mid: #333333;
    --gold: #d0a64a;
    --gold-faint: rgba(208, 166, 74, 0.10);
    --text-light: #ececec;
    --photo-top: #3a3a3c;
    --photo-bottom: #1c2230;
  }
  * { margin: 0; padding: 0; box-sizing: border-box; }
  html, body { width: 1200px; height: 900px; overflow: hidden; background: var(--bg); }
  .canvas { position: relative; width: 1200px; height: 900px; }

  .card {
    position: absolute; width: 552px; height: 368px; overflow: hidden;
    background: linear-gradient(180deg, var(--card-mid) 0%, var(--card-dark) 100%);
    box-shadow: 0 6px 16px rgba(0,0,0,0.25);
  }
  .card-front { left: 178px; top: 80px; z-index: 2; }
  .card-back  { left: 508px; top: 426px; z-index: 1; }

  /* Front */
  .intro {
    position: absolute; left: 10px; top: 38px; width: 248px; text-align: center;
    font-family: "Raleway", sans-serif; font-size: 11.5px; line-height: 14px; color: var(--text-light);
  }
  .surgeon-name {
    font-family: "Libre Baskerville", serif; font-size: 19px; line-height: 26px;
    color: var(--gold); margin: 1px 0 2px; white-space: nowrap;
  }
  .highlights {
    position: absolute; left: 44px; top: 124px; list-style: none;
    font-family: "Raleway", sans-serif; font-size: 11.5px; line-height: 16.8px; color: var(--text-light);
  }
  .highlights li { position: relative; padding-left: 14px; }
  .highlights li::before {
    content: ""; position: absolute; left: 0; top: 6px; width: 4px; height: 4px;
    border-radius: 50%; background: var(--gold);
  }
  .highlights .offer { color: var(--gold); font-size: 14px; line-height: 17px; margin-top: 1px; }
  .highlights .offer::before { top: 7px; }
  .savings { color: var(--text-light); display: block; }
  .booking { font-style: italic; font-size: 11px; color: var(--text-light); display: block; margin-top: 2px; }
  .refreshments {
    position: absolute; left: 38px; top: 321px;
    font-family: "Raleway", sans-serif; font-size: 13.5px; color: var(--gold);
  }
  .surgeon-photo {
    position: absolute; left: 298px; top: 0; width: 254px; height: 368px;
    background: linear-gradient(180deg, var(--photo-top) 0%, var(--photo-bottom) 100%);
  }
  .brand-seal {
    position: absolute; left: 268px; top: 80px; width: 100px; height: 100px;
    border: 2px solid var(--gold); border-radius: 50%;
    display: flex; align-items: center; justify-content: center;
    font-family: "Raleway", sans-serif; font-size: 24px; letter-spacing: 2px; color: var(--gold);
  }

  /* Back */
  .rsvp {
    position: absolute; left: 44px; top: 48px;
    font-family: "Poppins", sans-serif; font-size: 11.5px; line-height: 14.5px; color: var(--text-light);
  }
  .social { position: absolute; left: 44px; top: 98px; list-style: none; }
  .social li {
    display: flex; align-items: center; gap: 6px;
    font-family: "Poppins", sans-serif; font-size: 18px; line-height: 25px; color: var(--gold);
  }
  .social .dot { width: 14px; height: 14px; border-radius: 50%; background: var(--gold); }
  .details {
    position: absolute; left: 44px; top: 176px;
    font-family: "Poppins", sans-serif; font-size: 11.5px; line-height: 14.5px; color: var(--text-light);
  }
  .details dt { color: var(--gold); }
  .details dd { margin-bottom: 5px; }
  .website {
    position: absolute; left: 45px; top: 311px;
    font-family: "Poppins", sans-serif; font-size: 12px; color: var(--gold);
  }
  .brand-watermark {
    position: absolute; left: 266px; top: 58px; width: 272px; height: 272px;
    border: 3px solid var(--gold-faint); border-radius: 50%;
    display: flex; align-items: center; justify-content: center;
    font-family: "Poppins", sans-serif; font-size: 64px; letter-spacing: 4px; color: var(--gold-faint);
  }
</style>
</head>
<body>
<main class="canvas">

  <section class="card card-front">
    <div class="intro">
      <p>Join us for an exclusive event<br>with Double Board Certified Plastic Surgeon</p>
      <h1 class="surgeon-name">Tomas R. Belvino, MD</h1>
      <p>To learn more about the latest trends<br>in Cosmetic Plastic Surgery</p>
    </div>
    <ul class="highlights">
      <li>Breast Augmentation</li>
      <li>Cosmetic Breast Surgery</li>
      <li>Mommy Makeovers</li>
      <li>Facial Aging</li>
      <li>Live Demonstrations</li>
      <li>Mini Consultations</li>
      <li>Enter to win raffles and prizes</li>
      <li class="offer">Take advantage of our exclusive<br>Event Only pricing :
        <span class="savings">($500-$1000 savings)</span>
        <span class="booking">for booking your procedure.</span>
      </li>
    </ul>
    <p class="refreshments">Hors d'oeuvres will be served</p>
    <div class="surgeon-photo" role="img" aria-label="Portrait photo of the surgeon in a dark suit and tie"></div>
    <div class="brand-seal">LVR</div>
  </section>

  <section class="card card-back">
    <div class="brand-watermark">LVR</div>
    <p class="rsvp">Please RSVP by June 14, 2019<br>to belvinoMD@mailvexa.com<br>or DM on instagram</p>
    <ul class="social">
      <li><span class="dot"></span>@belvinoMD</li>
      <li><span class="dot"></span>LVR Plastic Surgery</li>
    </ul>
    <dl class="details">
      <dt>When:</dt>
      <dd>June 27, 2019&nbsp; (4p-6p)</dd>
      <dt>Where:</dt>
      <dd>Harwick Medical Pavilion<br>2718 N. 61st Street, Suite 305<br>Oak Lawn, IL 60917</dd>
      <dt>Phone:</dt>
      <dd>(708) 555-0173</dd>
    </dl>
    <p class="website">www.LVRplasticsurg.example</p>
  </section>

</main>
</body>
</html>
```